Islara Sunscreen

I need 2 labels for 2 sunscreens.
1: 50SPF Sunscreen suitable for oily and acne prone skin ( elexir from maltese plants that help with excess oil)
2: 50SPF Sunscreen suitable for normal skin made out of essential oils that help to calm down nervous system and stimulate sensation of relaxation.

Not sure if its too much writing on the label ?

Attached is the logo and picture of the bottle, beige tannish color 50ml

I wanted to include : Product of Malta on the label with maltese flag ( i guess smaller than the rest of the text)
I can only use " suitable" and "helps" as it is cosmetic and not medical.

Target Market(s)

Men and women

Industry/Entity Type

Skin care

Requirements
Must have
• Logo, descripción, Islara flag “ product of Malta. Incorporate Islara landscape like in the picture, use Islara clover flower like in picture attached.
Nice to have
• I want the label to be very Islara. Depict the landscape of the picture attached, use clover flower, use the Islara lady logo

```html
<!DOCTYPE html>
<html lang="en">
<head>
<meta charset="utf-8">
<title>Islara 50SPF Sunscreen Label</title>
<link rel="stylesheet" href="https://fonts.googleapis.com/css2?family=Jost:wght@400;500;600&display=swap">
<style>
  :root {
    --backdrop: #e4e2e0;
    --tube: #ecd9ca;
    --tube-edge: #e2cbb9;
    --cap: #e9d6c7;
    --ink: #3b3b3d;
    --ink-soft: #5a5a5c;
    --rule: #6e6e70;
    --hill: #8fbf6a;
    --field: #f2c7dc;
    --bloom: #c2249a;
    --flag-white: #f4f1ec;
    --flag-red: #c8161d;
  }
  * { margin: 0; padding: 0; box-sizing: border-box; }
  html, body { width: 1200px; height: 1200px; overflow: hidden; }
  body {
    background: var(--backdrop);
    font-family: "Jost", sans-serif;
    color: var(--ink);
    position: relative;
  }
  .tube-face {
    position: absolute;
    left: 380px; top: 60px;
    width: 440px; height: 1080px;
    background: var(--tube);
    border-radius: 10px 10px 36px 36px;
    box-shadow: inset 0 0 0 1px var(--tube-edge);
    overflow: hidden;
  }
  .crimp {
    position: absolute; left: 0; top: 0; width: 100%; height: 44px;
    background: repeating-linear-gradient(90deg, var(--tube) 0 6px, var(--tube-edge) 6px 8px);
  }
  .brand {
    position: absolute; top: 250px; width: 100%; text-align: center;
  }
  .brand-name {
    font-size: 58px; font-weight: 400; letter-spacing: 2px; line-height: 1;
    color: var(--ink);
  }
  .brand-tag {
    margin-top: 10px; font-size: 11px; font-weight: 400; letter-spacing: 1.6px;
    color: var(--ink);
  }
  .product {
    position: absolute; top: 375px; width: 100%; text-align: center;
    color: var(--ink-soft); font-weight: 400;
  }
  .product-spf { font-size: 44px; letter-spacing: 2px; line-height: 1.05; }
  .product-type { font-size: 46px; letter-spacing: 3px; line-height: 1.05; }
  .product-rule {
    width: 156px; height: 1px; background: var(--rule); margin: 10px auto 16px;
  }
  .product-suit {
    font-size: 15.5px; letter-spacing: 2px; line-height: 1.15; color: var(--ink-soft);
  }
  .landscape {
    position: absolute; left: 86px; top: 552px; width: 268px; height: 236px;
    border-radius: 40% 40% 48% 48%;
    background: linear-gradient(180deg, var(--hill) 0%, #c8b39a 18%, var(--field) 38%, #e79bc9 62%, var(--bloom) 86%);
    -webkit-mask-image: radial-gradient(ellipse 70% 70% at 50% 50%, #000 60%, transparent 100%);
            mask-image: radial-gradient(ellipse 70% 70% at 50% 50%, #000 60%, transparent 100%);
  }
  .origin {
    position: absolute; top: 798px; width: 100%; text-align: center; z-index: 2;
  }
  .origin-flag { display: block; margin: 0 auto; }
  .origin-text {
    margin-top: 6px; font-size: 12px; font-weight: 600; letter-spacing: 0.4px; color: var(--ink);
  }
  .cap {
    position: absolute; left: 0; bottom: 0; width: 100%; height: 170px;
    background: var(--cap);
    border-top: 1px solid var(--tube-edge);
  }
  .cap-notch {
    position: absolute; left: 175px; bottom: 40px; width: 90px; height: 80px;
    border: 1px solid var(--tube-edge); border-bottom: none; border-radius: 12px 12px 0 0;
  }
</style>
</head>
<body>
  <main class="tube-face">
    <div class="crimp"></div>

    <header class="brand">
      <div class="brand-name">Islara</div>
      <div class="brand-tag">NATURAL SKIN COSMETICS</div>
    </header>

    <section class="product">
      <div class="product-spf">50SPF</div>
      <div class="product-type">SUNSCREEN</div>
      <div class="product-rule"></div>
      <div class="product-suit">SUITABLE FOR OILY AND<br>ACNE PRONE SKIN</div>
    </section>

    <div class="landscape" role="img" aria-label="Painted Maltese landscape with green hills and a field of pink and magenta clover flowers"></div>

    <footer class="origin">
      <svg class="origin-flag" width="110" height="44" viewBox="0 0 110 44" aria-label="Flag of Malta">
        <rect x="0" y="2" width="55" height="40" fill="var(--flag-white)"/>
        <rect x="55" y="2" width="55" height="40" fill="var(--flag-red)"/>
      </svg>
      <div class="origin-text">MADE IN MALTA</div>
    </footer>

    <div class="cap"><div class="cap-notch"></div></div>
  </main>
</body>
</html>
```